Logo-Design für Managementberatung
Zielgruppe
Managementberatung (Schwerpunkt Strategieberatung) seriös und modern, agil und erfahren, lösungsorientiert.
Ich bringe Sie und Ihr Team, zur eigenen Zielfindung und dem zielorientierten Handeln - dem Schlüssel zum Erfolg.
Menschen, Teams und Unternehmen – werden mit Methode effektiver. Eine Anleitung zum Aufbau eines Systems zur zielgerichteten und modernen Unternehmensführung. (siehe auch beigefügte Datei)
Aufgabenstellung
Bitte entwickeln Sie ein Logo in der Varianten mit Claim und liefern dann einmal auch ohne Claim.
Sollten Sie mit Farben arbeiten, orientieren Sie sich bitte an dem in der Datei dargestellten Grün.
Dies entspricht dem Farbkonzept auf der neu zu konzipierender Webseite (siehe Demo auf blaukante.de).

```html
<!DOCTYPE html>
<html lang="de">
<head>
<meta charset="utf-8">
<title>Blaukante – Geschäftsausstattung</title>
<link href="https://fonts.googleapis.com/css2?family=Montserrat:wght@600&family=Open+Sans:wght@400;600;700&display=swap" rel="stylesheet">
<style>
  :root {
    --stage: #bcbdc0;
    --paper: #ffffff;
    --slate: #5e6b6b;
    --green: #55ab4b;
    --ink: #1d1d1b;
    --brand-font: 'Montserrat', sans-serif;
    --text-font: 'Open Sans', sans-serif;
  }
  * { margin: 0; padding: 0; box-sizing: border-box; }
  html, body { width: 711px; height: 1200px; overflow: hidden; background: var(--stage); }
  body { position: relative; font-family: var(--text-font); color: var(--ink); }

  .card, .letterhead { position: absolute; }
  .card { top: 95px; width: 222px; height: 144px; overflow: hidden; }
  .card--front { left: 112px; background: var(--paper); }
  .card--back { left: 395px; background: var(--slate); }

  .brand-mark { display: block; background: var(--green); }
  .brand-name { font-family: var(--text-font); font-weight: 700; color: var(--green); letter-spacing: 0.5px; white-space: nowrap; }
  .brand-claim { font-family: var(--brand-font); font-weight: 600; white-space: nowrap; }

  /* front card */
  .card--front .brand { position: absolute; right: 15px; top: 27px; display: flex; align-items: flex-start; gap: 6px; }
  .card--front .brand-mark { width: 17px; height: 17px; margin-top: 1px; }
  .card--front .brand-name { font-size: 15px; line-height: 16px; }
  .card--front .brand-claim { font-size: 6px; color: var(--slate); margin-top: 1px; }
  .card-person { position: absolute; left: 12px; top: 78px; font-size: 7.5px; font-weight: 600; color: var(--green); }
  .contact-list { list-style: none; position: absolute; left: 12px; top: 98px; font-size: 6.5px; line-height: 11px; }
  .contact-list li { display: flex; align-items: center; gap: 6px; }
  .contact-icon { width: 5px; height: 6px; fill: var(--green); flex: none; }
  .card-address { position: absolute; right: 15px; top: 98px; font-size: 6.5px; line-height: 11px; text-align: right; font-style: normal; }
  .card-footer { position: absolute; left: 0; bottom: 0; width: 222px; height: 9px; }
  .card-footer .web { position: absolute; right: 15px; bottom: 0; font-size: 6.5px; line-height: 8px; color: var(--paper); }

  /* back card */
  .card--back .brand { position: absolute; left: 0; right: 0; top: 34px; display: flex; flex-direction: column; align-items: center; }
  .card--back .brand-mark { width: 32px; height: 32px; }
  .card--back .brand-name { font-size: 17px; line-height: 18px; margin-top: 19px; color: var(--paper); }
  .card--back .brand-claim { font-size: 6.8px; color: var(--paper); margin-top: 3px; }

  /* letterhead */
  .letterhead { left: 77px; top: 280px; width: 558px; height: 785px; background: var(--paper); overflow: hidden; }
  .letterhead .brand { position: absolute; right: 37px; top: 41px; display: flex; align-items: flex-start; gap: 11px; }
  .letterhead .brand-mark { width: 28px; height: 28px; margin-top: 2px; }
  .letterhead .brand-name { font-size: 27px; line-height: 30px; }
  .letterhead .brand-claim { font-size: 10.5px; color: var(--slate); margin-top: 1px; }
  .sender-line { position: absolute; left: 59px; top: 124px; width: 150px; padding-bottom: 2px; border-bottom: 0.6px solid var(--green); font-size: 6.5px; white-space: nowrap; }
  .sender-line strong { font-weight: 700; }
  .letter-contact { position: absolute; left: 434px; top: 124px; width: 86px; }
  .letter-contact .person { font-size: 9.5px; font-weight: 700; color: var(--green); line-height: 14px; }
  .letter-contact address { font-style: normal; font-size: 6.5px; line-height: 11px; margin-top: 3px; padding-bottom: 5px; border-bottom: 0.6px solid var(--green); }
  .letter-contact .contact-list { position: static; margin-top: 4px; }
  .letter-footer { position: absolute; left: 0; bottom: 0; width: 558px; height: 29px; }
  .letter-footer .web { position: absolute; right: 20px; top: 5px; font-size: 10.5px; color: var(--paper); }
</style>
</head>
<body>

  <section class="card card--front" aria-label="Visitenkarte Vorderseite">
    <div class="brand">
      <span class="brand-mark"></span>
      <div>
        <div class="brand-name">BLAUKANTE</div>
        <div class="brand-claim">Klar · Gezielt · Wirksam</div>
      </div>
    </div>
    <p class="card-person">Jonas Nordhallm</p>
    <ul class="contact-list">
      <li><svg class="contact-icon" viewBox="0 0 5 6"><rect width="5" height="6" rx="0.8"/></svg>+49 (0)170 5550123</li>
      <li><svg class="contact-icon" viewBox="0 0 5 6"><path d="M0 2h5v4H0z M0 2l2.5 1.8L5 2"/></svg>nordhallm@blaukante.de</li>
    </ul>
    <address class="card-address">Am Kranzhof 12<br>50667 Köln</address>
    <div class="card-footer">
      <svg width="222" height="9" viewBox="0 0 222 9">
        <rect x="0" y="0" width="142" height="2" fill="var(--slate)"/>
        <rect x="0" y="3.5" width="145" height="5.5" fill="var(--green)"/>
        <polygon points="146,9 152,0 222,0 222,9" fill="var(--green)"/>
      </svg>
      <span class="web">www.blaukante.de</span>
    </div>
  </section>

  <section class="card card--back" aria-label="Visitenkarte Rückseite">
    <div class="brand">
      <span class="brand-mark"></span>
      <div class="brand-name">BLAUKANTE</div>
      <div class="brand-claim">Klar · Gezielt · Wirksam</div>
    </div>
  </section>

  <section class="letterhead" aria-label="Briefbogen">
    <div class="brand">
      <span class="brand-mark"></span>
      <div>
        <div class="brand-name">BLAUKANTE</div>
        <div class="brand-claim">Klar · Gezielt · Wirksam</div>
      </div>
    </div>
    <p class="sender-line"><strong>Blaukante</strong>&nbsp; - &nbsp;Am Kranzhof 12&nbsp; - &nbsp;50667 Köln</p>
    <div class="letter-contact">
      <p class="person">Jonas Nordhallm</p>
      <address>Am Kranzhof 12<br>50667 Köln</address>
      <ul class="contact-list">
        <li><svg class="contact-icon" viewBox="0 0 5 6"><rect width="5" height="6" rx="0.8"/></svg>+49 (0)170 5550123</li>
        <li><svg class="contact-icon" viewBox="0 0 5 6"><path d="M0 2h5v4H0z M0 2l2.5 1.8L5 2"/></svg>nordhallm@blaukante.de</li>
      </ul>
    </div>
    <div class="letter-footer">
      <svg width="558" height="29" viewBox="0 0 558 29">
        <rect x="0" y="13" width="426" height="3" fill="var(--green)"/>
        <polygon points="0,19 419,19 414,29 0,29" fill="var(--slate)"/>
        <polygon points="421,29 437,0 558,0 558,29" fill="var(--green)"/>
      </svg>
      <span class="web">www.blaukante.de</span>
    </div>
  </section>

</body>
</html>
```